Business card design needed

I need a business card for my private practice. I would like to see the designs that use bright blue and white. I would like to see similar designs as to the card below:
http://blog.printmoss.com/2009/designing-a-business-card-with-pm-kt517-template.html
I would like to see the back of the card have room for appointment times. Thank you.

Industry/Entity Type
Business
Contact Information for Business Card
Tandem Wellbeing & Guidance Services
Fiona Marsh B.Psychology
Registered Psychologist
Building C, Level 3, 14 Wattle Crescent, Canberra, ACT 2601
T: (02) 6248 7315
F: (02) 6248 7390
info@tandemwellbeing.com.au
www.tandemwellbeing.com.au

```html
<!DOCTYPE html>
<html lang="en">
<head>
<meta charset="utf-8">
<title>Tandem Wellbeing &amp; Guidance Services – Business Card</title>
<link href="https://fonts.googleapis.com/css2?family=Old+Standard+TT:wght@400;700&display=swap" rel="stylesheet">
<style>
  :root {
    --navy: #29246b;
    --ink: #1b1b1b;
    --paper: #ffffff;
    --backdrop-light: #e4e4e4;
    --backdrop-dark: #bdbdbd;
  }
  * { box-sizing: border-box; margin: 0; padding: 0; }
  html, body { width: 1200px; height: 985px; overflow: hidden; }
  body {
    background: radial-gradient(ellipse at 50% 45%, var(--backdrop-light), var(--backdrop-dark));
    font-family: "Old Standard TT", Georgia, serif;
    position: relative;
  }
  .card {
    position: absolute;
    left: 250px;
    width: 700px;
    height: 428px;
    border-radius: 26px;
    overflow: hidden;
    box-shadow: 0 10px 24px rgba(0,0,0,.22);
  }
  /* Back */
  .card--back {
    top: 30px;
    background: var(--navy);
    display: flex;
    align-items: center;
    justify-content: center;
  }
  .brand {
    display: flex;
    align-items: center;
    gap: 16px;
    font-weight: 700;
    line-height: 1.15;
  }
  .brand__square { width: 54px; height: 54px; flex: none; }
  .brand__name { font-size: 24px; }
  .card--back .brand { color: var(--paper); }
  .card--back .brand__square { background: var(--paper); }

  /* Front */
  .card--front { top: 500px; background: var(--paper); color: var(--ink); }
  .accent { position: absolute; background: var(--navy); }
  .accent--top-left { left: 0; top: 40px; width: 16px; height: 130px; }
  .accent--bottom-right { right: 0; bottom: 40px; width: 16px; height: 130px; }
  .divider {
    position: absolute;
    left: 355px; top: 40px;
    width: 5px; height: 230px;
    background: var(--navy);
  }
  .card--front .brand {
    position: absolute;
    left: 56px; top: 70px;
    width: 280px;
    color: var(--navy);
  }
  .card--front .brand__square { background: var(--navy); width: 46px; height: 46px; }
  .card--front .brand__name { font-size: 20px; }

  .appointment { font-size: 18px; letter-spacing: .5px; }
  .appointment__title {
    position: absolute; left: 40px; top: 226px;
    color: var(--navy); font-size: 21px;
  }
  .appointment__row {
    position: absolute;
    display: flex; gap: 12px;
  }
  .appointment__row--day-date { left: 40px; width: 300px; top: 290px; }
  .appointment__row--time { left: 385px; width: 275px; top: 372px; }
  .field { display: flex; align-items: baseline; flex: 1; white-space: nowrap; }
  .field__fill {
    flex: 1; margin-left: 6px;
    border-bottom: 2px dotted var(--ink);
    height: 1px; transform: translateY(-4px);
  }

  .contact {
    position: absolute;
    left: 385px; top: 42px; right: 40px;
    letter-spacing: .6px;
  }
  .contact__name { font-size: 28px; color: var(--ink); line-height: 1.2; }
  .contact__name .given { color: var(--navy); }
  .contact__credential { color: var(--navy); font-size: 18px; margin-top: 2px; }
  .contact__role { font-size: 18px; }
  .contact__address { font-size: 16px; margin: 8px 0 0 30px; line-height: 1.3; }
  .contact__phones { font-size: 16px; margin: 6px 0 0 30px; line-height: 1.4; }
  .contact__phones span { display: inline-block; width: 26px; }
  .contact__web { color: var(--navy); font-size: 15px; margin-top: 6px; line-height: 1.35; }
</style>
</head>
<body>
  <section class="card card--back" aria-label="Card back">
    <div class="brand">
      <div class="brand__square"></div>
      <div class="brand__name">Tandem Wellbeing &amp;<br>Guidance Services</div>
    </div>
  </section>

  <section class="card card--front" aria-label="Card front">
    <div class="accent accent--top-left"></div>
    <div class="accent accent--bottom-right"></div>

    <div class="brand">
      <div class="brand__square"></div>
      <div class="brand__name">Tandem Wellbeing &amp;<br>Guidance Services</div>
    </div>

    <div class="divider"></div>

    <div class="contact">
      <p class="contact__name"><span class="given">Fiona</span> Marsh</p>
      <p class="contact__credential">B.Psychology</p>
      <p class="contact__role">Psychologist</p>
      <p class="contact__address">Building C, Level 3<br>14 Wattle Crescent<br>Canberra, ACT 2601</p>
      <p class="contact__phones"><span>T</span>(02) 6248 7315<br><span>F</span>(02) 6248 7390</p>
      <p class="contact__web">info@tandemwellbeing.com.au<br>www.tandemwellbeing.com.au</p>
    </div>

    <div class="appointment">
      <p class="appointment__title">Next appointment</p>
      <div class="appointment__row appointment__row--day-date">
        <div class="field">Day<span class="field__fill"></span></div>
        <div class="field">Date<span class="field__fill"></span></div>
      </div>
      <div class="appointment__row appointment__row--time">
        <div class="field">Time<span class="field__fill"></span></div>
      </div>
    </div>
  </section>
</body>
</html>
```